Stationery & Business card for childrens education company
MAPLEWING LEARNING
Stationery & Business card for childrens education company - Education
Creative Brief
Use same font as used in my logo
georgia font
Professional
Rina Holcombe
Managing Director
Level 2 417 Farrowby Lane Melbourne, Victoria 3000
admin@maplewing.com.au
www.maplewing.com.au

```html
<!DOCTYPE html>
<html lang="en">
<head>
<meta charset="utf-8">
<title>Maplewing Learning — Stationery Suite</title>
<link href="https://fonts.googleapis.com/css2?family=Gelasio:wght@400;700&family=Dancing+Script:wght@600&display=swap" rel="stylesheet">
<style>
  :root{
    --red:#c4161c;
    --red-dark:#9e0f14;
    --ink:#2a2a2a;
    --grey:#8c8c8c;
    --rule:#d9d9d9;
    --paper:#ffffff;
    --backdrop:#e8e6e3;
    --faint:#efefef;
  }
  *{box-sizing:border-box;margin:0;padding:0}
  html,body{width:1200px;height:530px;overflow:hidden}
  body{background:var(--backdrop);font-family:"Gelasio",Georgia,serif;color:var(--ink);position:relative}
  .sheet{position:absolute;background:var(--paper);box-shadow:0 2px 6px rgba(0,0,0,.18);overflow:hidden}
  .brand{display:flex;align-items:center;gap:5px;color:var(--red);font-weight:700;letter-spacing:.04em;white-space:nowrap}
  .brand-mark{width:9px;height:9px;background:var(--ink);flex:none}
  .brand.on-red{color:var(--paper)}
  .brand.on-red .brand-mark{background:var(--paper)}
  .watermark{position:absolute;border-radius:50%;background:var(--faint)}
  .footer-text{position:absolute;left:0;right:0;text-align:center;font-size:5px;color:var(--grey)}
  .footer-band{position:absolute;left:0;right:0;bottom:0;height:6px;background:var(--red)}

  /* letterheads */
  .letterhead{width:270px;height:382px}
  .letterhead .brand{position:absolute;left:20px;top:22px;font-size:10px}
  .letterhead .watermark{width:110px;height:110px;right:26px;bottom:60px}
  .letterhead .footer-text{bottom:14px}
  .lh-back{left:205px;top:22px}
  .lh-front{left:150px;top:72px}

  /* invoice */
  .invoice{width:270px;height:382px}
  .inv-back{left:548px;top:22px}
  .inv-front{left:494px;top:76px}
  .invoice .brand{position:absolute;left:20px;top:22px;font-size:10px}
  .inv-title{position:absolute;right:22px;top:40px;font-size:13px;color:var(--red);font-weight:700;letter-spacing:.05em}
  .inv-meta{position:absolute;right:22px;top:60px;font-size:5.5px;color:var(--ink);line-height:1.9;text-align:right}
  .inv-meta span{display:inline-block;width:48px;border-bottom:1px solid var(--rule);margin-left:4px}
  .bill-to{position:absolute;left:20px;top:64px;width:90px;font-size:5.5px;color:var(--grey)}
  .bill-to i{display:block;height:8px;border-bottom:1px solid var(--rule)}
  .inv-table{position:absolute;left:20px;top:112px;width:230px;border-collapse:collapse;font-size:5.5px}
  .inv-table th{background:var(--red);color:var(--paper);font-weight:700;padding:3px 4px;text-align:left;letter-spacing:.05em}
  .inv-table td{height:10.5px;border:1px solid var(--rule)}
  .inv-totals{position:absolute;right:20px;top:306px;font-size:5.5px;line-height:1.8;text-align:right}
  .inv-totals span{display:inline-block;width:40px;border:1px solid var(--rule);height:8px;vertical-align:middle;margin-left:4px}
  .inv-thanks{position:absolute;left:20px;top:308px;font-size:6px;font-style:italic;color:var(--grey)}
  .inv-sign{position:absolute;left:20px;top:340px;font-size:5.5px;color:var(--grey)}
  .inv-sign span{display:inline-block;width:70px;border-bottom:1px solid var(--rule);margin-left:3px}
  .invoice .footer-text{bottom:14px}

  /* business cards */
  .card{width:88px;height:52px}
  .card-front .brand{position:absolute;left:7px;top:5px;font-size:4.6px;gap:3px}
  .card-front .brand-mark{width:5px;height:5px}
  .card-front .who{position:absolute;left:7px;top:13px;font-size:3.8px;line-height:1.2}
  .card-front .who b{font-size:4.4px;color:var(--red)}
  .card-front .band{position:absolute;left:0;right:0;bottom:0;height:4px;background:var(--red)}
  .card-back{background:var(--red)}
  .card-back .brand{position:absolute;left:50%;top:50%;transform:translate(-50%,-50%);font-size:5.5px;gap:3px}
  .card-back .brand-mark{width:6px;height:6px}
  .card-back .web{position:absolute;bottom:5px;left:0;right:0;text-align:center;font-size:3.6px;color:var(--paper)}
  .c1{left:18px;top:300px}.c2{left:18px;top:360px}
  .c3{left:112px;top:300px}.c4{left:112px;top:360px}

  /* small envelope front */
  .small-env{left:738px;top:196px;width:160px;height:106px}
  .small-env .brand{position:absolute;left:12px;top:12px;font-size:6.5px;gap:4px}
  .small-env .brand-mark{width:7px;height:7px}
  .small-env .return{position:absolute;left:12px;top:25px;font-size:4px;color:var(--grey);line-height:1.4}
  .small-env .band{position:absolute;left:0;right:0;bottom:0;height:20px;background:var(--red)}
  .small-env .band span{position:absolute;right:10px;top:7px;font-size:4px;color:var(--paper)}

  /* compliment slip */
  .comp-slip{left:880px;top:100px;width:306px;height:148px}
  .comp-slip .brand{position:absolute;left:16px;top:16px;font-size:8px}
  .comp-slip .greeting{position:absolute;right:18px;top:12px;font-family:"Dancing Script",cursive;font-size:17px;color:var(--red)}
  .comp-slip .watermark{width:70px;height:70px;left:40px;bottom:24px}
  .comp-slip .footer-text{bottom:12px}
  .comp-slip .rule{position:absolute;left:16px;right:16px;top:40px;height:1px;background:var(--red)}

  /* DL envelope with open flap */
  .envelope{position:absolute;left:880px;top:330px;width:306px;height:150px}
  .envelope svg{position:absolute;inset:0}
  .envelope .brand{position:absolute;left:14px;top:14px;font-size:7px}
  .envelope .return{position:absolute;left:14px;top:28px;font-size:4.2px;color:var(--grey);line-height:1.4}
</style>
</head>
<body>

<section class="sheet letterhead lh-back" aria-label="Letterhead">
  <div class="brand"><span class="brand-mark"></span>MAPLEWING LEARNING</div>
  <div class="watermark"></div>
  <p class="footer-text">Maplewing Learning Pty Ltd · Level 2 417 Farrowby Lane Melbourne, Victoria 3000 · www.maplewing.com.au</p>
  <div class="footer-band"></div>
</section>
<section class="sheet letterhead lh-front" aria-label="Letterhead">
  <div class="brand"><span class="brand-mark"></span>MAPLEWING LEARNING</div>
  <div class="watermark"></div>
  <p class="footer-text">Maplewing Learning Pty Ltd · Level 2 417 Farrowby Lane Melbourne, Victoria 3000 · www.maplewing.com.au</p>
  <div class="footer-band"></div>
</section>

<section class="sheet invoice inv-back" aria-label="Invoice">
  <div class="brand"><span class="brand-mark"></span>MAPLEWING LEARNING</div>
  <div class="inv-title">INVOICE</div>
  <div class="footer-band"></div>
</section>
<section class="sheet invoice inv-front" aria-label="Invoice">
  <div class="brand"><span class="brand-mark"></span>MAPLEWING LEARNING</div>
  <div class="inv-title">INVOICE</div>
  <div class="inv-meta">INVOICE NUMBER<span></span><br>DATE<span></span></div>
  <div class="bill-to">BILL TO<i></i><i></i><i></i></div>
  <table class="inv-table">
    <thead><tr><th style="width:22%">QUANTITY</th><th>DESCRIPTION</th><th style="width:22%">TOTAL</th></tr></thead>
    <tbody>
      <tr><td></td><td></td><td></td></tr><tr><td></td><td></td><td></td></tr>
      <tr><td></td><td></td><td></td></tr><tr><td></td><td></td><td></td></tr>
      <tr><td></td><td></td><td></td></tr><tr><td></td><td></td><td></td></tr>
      <tr><td></td><td></td><td></td></tr><tr><td></td><td></td><td></td></tr>
      <tr><td></td><td></td><td></td></tr><tr><td></td><td></td><td></td></tr>
      <tr><td></td><td></td><td></td></tr><tr><td></td><td></td><td></td></tr>
      <tr><td></td><td></td><td></td></tr><tr><td></td><td></td><td></td></tr>
    </tbody>
  </table>
  <p class="inv-thanks">Thank you for your business!</p>
  <div class="inv-totals">SUB TOTAL<span></span><br>SALES TAX<span></span><br>TOTAL<span></span></div>
  <p class="inv-sign">Signature<span></span></p>
  <p class="footer-text">Maplewing Learning Pty Ltd · Level 2 417 Farrowby Lane Melbourne, Victoria 3000 · www.maplewing.com.au</p>
  <div class="footer-band"></div>
</section>

<article class="sheet card card-front c1" aria-label="Business card front">
  <div class="brand"><span class="brand-mark"></span>MAPLEWING LEARNING</div>
  <p class="who"><b>Rina Holcombe</b><br>Managing Director<br>Level 2 417 Farrowby Lane<br>Melbourne, Victoria 3000<br>M 0400 555 731 · Skype trholcombe<br>admin@maplewing.com.au</p>
  <div class="band"></div>
</article>
<article class="sheet card card-back c2" aria-label="Business card back">
  <div class="brand on-red"><span class="brand-mark"></span>MAPLEWING LEARNING</div>
  <p class="web">www.maplewing.com.au</p>
</article>
<article class="sheet card card-back c3" aria-label="Business card back">
  <div class="brand on-red"><span class="brand-mark"></span>MAPLEWING LEARNING</div>
  <p class="web">www.maplewing.com.au</p>
</article>
<article class="sheet card card-back c4" aria-label="Business card back">
  <div class="brand on-red"><span class="brand-mark"></span>MAPLEWING LEARNING</div>
  <p class="web">www.maplewing.com.au</p>
</article>

<section class="sheet small-env" aria-label="Small envelope">
  <div class="brand"><span class="brand-mark"></span>MAPLEWING LEARNING</div>
  <p class="return">Level 2 417 Farrowby Lane<br>Melbourne, Victoria 3000</p>
  <div class="band"><span>www.maplewing.com.au</span></div>
</section>

<section class="sheet comp-slip" aria-label="Compliment slip">
  <div class="brand"><span class="brand-mark"></span>MAPLEWING LEARNING</div>
  <p class="greeting">With Compliments!</p>
  <div class="rule"></div>
  <div class="watermark"></div>
  <p class="footer-text">Level 2 417 Farrowby Lane Melbourne, Victoria 3000 · admin@maplewing.com.au · www.maplewing.com.au</p>
  <div class="footer-band"></div>
</section>

<section class="envelope" aria-label="DL envelope">
  <svg width="306" height="150" viewBox="0 0 306 150">
    <rect x="0" y="0" width="250" height="150" fill="#ffffff" style="filter:drop-shadow(0 2px 3px rgba(0,0,0,.18))"/>
    <path d="M250 0 L306 40 L306 110 L250 150 Z" fill="#f4f4f4" stroke="#dcdcdc"/>
    <path d="M250 0 L218 75 L250 150" fill="none" stroke="#e2e2e2"/>
    <rect x="0" y="142" width="250" height="8" fill="var(--red)"/>
  </svg>
  <div class="brand"><span class="brand-mark"></span>MAPLEWING LEARNING</div>
  <p class="return">Level 2 417 Farrowby Lane<br>Melbourne, Victoria 3000</p>
</section>

</body>
</html>
```